Stationary for a Hand Therapy Clinic
Letterhead/banner, envelopes, business cards
Stationary for a Hand Therapy Clinic - Health
Creative Brief
Professional
Miriam Dorsey, OTD, OTR/L, CHT
Certified Hand Therapist
27548 52nd Ave W Ste 118 Lynnwood, WA 98036
miriam@palmrestcare.example
www.palmrestcare.example
I am open to ideas for placement of: Elbows - Wrists - Fingers (replace dashes with dots) and We guide each step toward fuller days.
We guide each step toward fuller days
miriamdorsey miriamdorsey
Windowed and standard envelopes both are appreciated too! Also, a half sheet sized folder is also great.
One additional item we will need is design for a name tag. Current ones are approximately 1x3" or 1.5x3.5" or so. Likely including the logo, employee's first name and title, such as Certified Hand Therapist, Occupational Therapist, Licensed OT Assistant, Operations Manager, and Patient Care Coordinator.
We definitely prefer orange over green as the primary color for the back side of the business cards and in stationary/other products.
Please use design from entry #439 in our logo contest, replacing dashes with dots. FONT: NEXA BOLD (Or your discretion; others possible) PRIMARY COLORS: ORANGE (#D18122) AND GREEN (#738F52) ACCENT COLORS: BROWN (#544741), LIGHT GREEN (#B9C4AC), RED #993B2C, OR BLUE (#538898) BLACK (#2F3334) WHITE (F0F1E8) PLEASE do not use logos/image from our current website. It will be updated with the new logo.

```html
<!DOCTYPE html>
<html lang="en">
<head>
<meta charset="utf-8">
<title>Palm Rest Care — Note Card</title>
<link href="https://fonts.googleapis.com/css2?family=Montserrat:ital,wght@0,500;0,600;0,700;1,700&display=swap" rel="stylesheet">
<style>
  :root {
    --orange: #d18122;
    --green: #738f52;
    --white: #ffffff;
    --paper-shade: #f3f3f3;
    --backdrop: #e4e4e4;
    --text-light: #fbe9d4;
  }
  * { box-sizing: border-box; margin: 0; padding: 0; }
  html, body { width: 1200px; height: 854px; overflow: hidden; }
  body {
    background: var(--backdrop);
    font-family: "Montserrat", sans-serif;
    position: relative;
  }
  .panel {
    position: absolute;
    box-shadow: 0 2px 8px rgba(0,0,0,0.12);
  }
  .card-front {
    left: 101px; top: 115px; width: 494px; height: 298px;
    background: linear-gradient(90deg, var(--paper-shade), var(--white) 45%, var(--paper-shade));
  }
  .brand {
    position: absolute; left: 48px; top: 110px;
    display: flex; align-items: center; gap: 16px;
  }
  .brand-mark {
    width: 50px; height: 50px; border-radius: 50%;
    background: var(--orange);
    flex: none;
  }
  .brand-name {
    font-weight: 700; font-size: 30px; color: var(--orange);
    letter-spacing: 0.5px; line-height: 1; white-space: nowrap;
  }
  .brand-line {
    margin-top: 7px; font-weight: 600; font-size: 11.5px;
    color: var(--green); letter-spacing: 4px; text-transform: uppercase;
    white-space: nowrap;
  }
  .tagline-band {
    position: absolute; left: 0; bottom: 0; width: 100%; height: 24px;
    background: var(--orange);
    border-top: 3px solid var(--green);
    display: flex; align-items: center; padding-left: 80px;
  }
  .tagline {
    color: var(--white); font-style: italic; font-weight: 700; font-size: 12px;
    white-space: nowrap;
  }
  .card-back {
    left: 101px; top: 449px; width: 494px; height: 295px;
    background: var(--orange);
  }
  .back-mark {
    position: absolute; left: 187px; top: 40px;
    width: 120px; height: 120px; border-radius: 50%;
    background: rgba(255,255,255,0.08);
  }
  .back-contact {
    position: absolute; left: 0; bottom: 14px; width: 100%;
    text-align: center; color: var(--text-light);
    font-size: 8px; font-weight: 500; line-height: 1.8;
  }
  .inside-top {
    left: 619px; top: 115px; width: 473px; height: 317px;
    background: var(--white);
  }
  .inside-bottom {
    left: 619px; top: 432px; width: 473px; height: 312px;
    background: linear-gradient(180deg, #ececec, var(--white) 45%);
  }
</style>
</head>
<body>
  <section class="panel card-front">
    <div class="brand">
      <div class="brand-mark"></div>
      <div>
        <div class="brand-name">PALM REST CARE</div>
        <div class="brand-line">Elbows • Wrists • Fingers</div>
      </div>
    </div>
    <div class="tagline-band">
      <p class="tagline">We guide each step toward fuller days</p>
    </div>
  </section>

  <section class="panel card-back">
    <div class="back-mark"></div>
    <div class="back-contact">
      <p>27548 52nd Ave W Ste 118 Cedarbrook, WA 98112</p>
      <p>www.palmrestcare.example</p>
    </div>
  </section>

  <section class="panel inside-top"></section>
  <section class="panel inside-bottom"></section>
</body>
</html>
```